Kitesurf Weather Forecast Application Needs an Advertising Banner

We need an Advertising Banner for our iOS Kitesurf Weather Forecast Application. The application name is GustMapper and you can download it from the Plum Depot.

https://apps.plumdepot-market.com/app/gustmapper-breeze-and-sky-outlook/id804417392?mt=8

The banner should have the logo of our application, which can be either found from the Plum Depot or uploaded on this post. It should describe what our app does with either words or graphic story. GustMapper is a weather forecast application for Kitesurfers. As the banner is small, animated gifs will also be considered.

We need the following sizes 320x50 and 728x90. The banner will be uploaded to tavlo. Tavlo accepts images in PNG, JPEG and GIF. We want it in one of the formats that can be uploaded to TavLo and vector .ai so we can make changed if necessary in the future.

On tap the banner will open Plum Depot on the user's device and present GustMapper.

06/09. I added a screenshot from an application that the banner will be added. The screenshot is from an Lumafon 4 Max (it is from a big device). The red area on the bottom is where the advert will go and it should be readable.

Target Market(s)

Banner will be displayed in other iOS Applications. One of them is Rigging Reckoner https://apps.plumdepot-market.com/us/app/rigging-reckoner/id937206148?mt=8

Industry/Entity Type

Advertising

Font styles to use
Other font styles liked:
• San Francisco

Requirements
Must have
• GustMapper logo and communicate a clear message on what the application does. GustMapper is a weather forecast application for Kitesurfers. If you want to find more information please visit the PlumDepot link provided.
Nice to have
• Animated gif will be nice to have, as the banner is small and it maybe difficult to communicate the message required.
Should not have
• We prefer something minimal and along the lines of our application design.

```html
<!DOCTYPE html>
<html lang="en">
<head>
<meta charset="utf-8">
<title>GustMapper banner sizes</title>
<link href="https://fonts.googleapis.com/css2?family=Open+Sans:wght@400;600&display=swap" rel="stylesheet">
<style>
  :root {
    --board: #464646;
    --label: #ffffff;
    --orange-deep: #ff7d00;
    --orange: #ffa000;
    --yellow: #ffb900;
    --text-light: #fff8e6;
    --art-blue: #4fb6c9;
    --art-green: #7cc36a;
    --logo-dark: #3a3a3a;
  }
  html, body {
    margin: 0;
    width: 1200px;
    height: 1200px;
    overflow: hidden;
    background: var(--board);
    font-family: "Open Sans", sans-serif;
  }
  .board { position: relative; width: 1200px; height: 1200px; }
  .size-label {
    position: absolute;
    left: 124px;
    margin: 0;
    color: var(--label);
    font-size: 35px;
    font-weight: 400;
    line-height: 1;
  }
  .banner {
    position: absolute;
    left: 124px;
    overflow: hidden;
    background: linear-gradient(90deg, var(--orange) 0%, var(--yellow) 38%, var(--orange) 75%, var(--orange-deep) 100%);
  }
  .banner > * { position: absolute; }
  .hero-art {
    border-radius: 4px;
    background: linear-gradient(135deg, var(--art-blue), var(--yellow) 55%, var(--art-green));
    opacity: .85;
  }
  .feature { color: var(--text-light); white-space: nowrap; margin: 0; }
  .feature::before { content: "➢"; position: absolute; left: -1.5em; }
  .feature span { display: block; }
  .brand-name { color: #fff; font-weight: 400; white-space: nowrap; line-height: 1; }
  .brand-mark { border-radius: 50%; background: var(--logo-dark); }

  /* 320 x 50 */
  .banner--small { top: 411px; width: 633px; height: 99px; }
  .banner--small .hero-art { left: 18px; top: 23px; width: 76px; height: 58px; }
  .banner--small .feature { font-size: 6px; line-height: 8px; font-weight: 600; }
  .banner--small .brand-name { left: 428px; top: 40px; font-size: 21px; }
  .banner--small .brand-mark { left: 568px; top: 25px; width: 52px; height: 52px; }

  /* 728 x 90 */
  .banner--large { top: 725px; width: 994px; height: 123px; }
  .banner--large .hero-art { left: 28px; top: 18px; width: 124px; height: 90px; }
  .banner--large .feature { font-size: 11px; line-height: 14px; }
  .banner--large .brand-name { left: 648px; top: 43px; font-size: 34px; }
  .banner--large .brand-mark { left: 862px; top: 19px; width: 84px; height: 84px; }
</style>
</head>
<body>
<div class="board">
  <h2 class="size-label" style="top:345px">320_50</h2>
  <div class="banner banner--small">
    <div class="hero-art" role="img" aria-label="Illustration of a phone showing weather forecast cards"></div>
    <p class="feature" style="left:126px;top:34px"><span>Weekly Forcast</span><span>(showing only kiteable spots)</span></p>
    <p class="feature" style="left:234px;top:34px"><span>Detailed Weather</span><span>(see hourly forcast and live)</span></p>
    <p class="feature" style="left:332px;top:34px"><span>Weather on Map</span><span>(get forcast and live data)</span></p>
    <p class="feature" style="left:126px;top:59px"><span>Live Weather</span><span>(check out live stations)</span></p>
    <p class="feature" style="left:234px;top:59px"><span>Weather on Map</span><span>(get forcast and live data)</span></p>
    <div class="brand-name">GustMapper</div>
    <div class="brand-mark"></div>
  </div>

  <h2 class="size-label" style="top:663px">728_90</h2>
  <div class="banner banner--large">
    <div class="hero-art" role="img" aria-label="Illustration of a phone showing weather forecast cards"></div>
    <p class="feature" style="left:190px;top:24px"><span>Weekly Forcast</span><span>(showing only kiteable spots)</span></p>
    <p class="feature" style="left:362px;top:24px"><span>Detailed Weather</span><span>(see hourly forcast and live)</span></p>
    <p class="feature" style="left:514px;top:24px"><span>Weather on Map</span><span>(get forcast and live data)</span></p>
    <p class="feature" style="left:190px;top:64px"><span>Live Weather</span><span>(check out live stations)</span></p>
    <p class="feature" style="left:362px;top:64px"><span>Weather on Map</span><span>(get forcast and live data)</span></p>
    <div class="brand-name">GustMapper</div>
    <div class="brand-mark"></div>
  </div>
</div>
</body>
</html>
```